Brevin K - Premium Business Cards

Background of Brevin K
Brevin Kaltwell is a cigar mobile lounge where guests become family. A place of luxury, relaxation, and ambiance is the global popularity demand. Brevin Kaltwell strives to provide first-class service of quality and products. Our goal is to ensure that every guest is treated and serviced as a VIP.

Brevin Kaltwell was founded by Dennis Marlow Jr in January 2020. After 15 years of cigar reviews and research Dennis decided it was time to launch his own cigar brand and boutique cigar company. With a wealth of knowledge and years of experience Brevin Kaltwell was born. With opulence for all cultures, Brevin Kaltwell offers hand rolled cigars with premium blend tobacco from sweet to bold imported from Costa Rica, Dominican Republic, and Nicaragua. Thank you for your business!

Objective:
Create a business card template to be used for all employees. Design should communicate premium and classy. And should use earth tone colors.

Design should include:
1. Client wants to incorporate the cigar leaf
2. Logo
3. Tagline: Respect the smoke
3. Content info:
Calvin Rusholm
Owner
614-587-3906
crusholm@brevinleafco.com
brevinkaltwell.com

```html
<!DOCTYPE html>
<html lang="en">
<head>
<meta charset="utf-8">
<title>Brevin Kaltwell – Business Card</title>
<link rel="stylesheet" href="https://fonts.googleapis.com/css2?family=Great+Vibes&family=Oswald:wght@400&family=Roboto:wght@400;700&display=swap">
<style>
  :root {
    --stage: #efeae3;
    --espresso: #3a1e10;
    --tobacco-gold: #efb96a;
    --gold-script: #e3a45c;
    --cream: #f3ece4;
    --ink: #231a14;
    --leaf-dark: rgba(120, 70, 40, 0.28);
    --leaf-warm: rgba(170, 110, 50, 0.45);
  }
  * { box-sizing: border-box; margin: 0; padding: 0; }
  html, body { width: 1200px; height: 1200px; overflow: hidden; }
  body {
    background: var(--stage);
    position: relative;
    font-family: "Roboto", Arial, sans-serif;
  }
  .card {
    position: absolute;
    left: 248px;
    width: 704px;
    height: 388px;
    overflow: hidden;
    box-shadow: 0 6px 16px rgba(0,0,0,0.18);
  }
  .card--front { top: 187px; background: var(--espresso); }
  .card--back  { top: 625px; background: var(--tobacco-gold); }

  .leaf-art { position: absolute; }
  .card--front .leaf-art {
    left: -10px; top: 180px; width: 170px; height: 220px;
    border-radius: 60% 40% 50% 50%;
    background: radial-gradient(ellipse at 40% 50%, var(--leaf-dark), rgba(120,70,40,0) 70%);
  }
  .card--back .leaf-art {
    left: 496px; top: 74px; width: 230px; height: 330px;
    border-radius: 55% 45% 40% 60% / 60% 50% 50% 40%;
    background: radial-gradient(ellipse at 45% 55%, var(--leaf-warm) 0%, rgba(170,110,50,0.3) 60%, rgba(170,110,50,0) 75%);
  }

  .holder-name {
    position: absolute; left: 0; right: 0; top: 118px;
    text-align: center; padding-left: 80px;
    font-family: "Great Vibes", cursive;
    font-size: 64px; color: var(--gold-script);
    line-height: 1;
  }
  .holder-role {
    position: absolute; top: 205px; left: 176px; width: 354px;
    display: flex; align-items: center; gap: 10px;
    font-family: "Oswald", sans-serif; font-size: 19px;
    color: var(--cream); letter-spacing: 0.5px;
  }
  .holder-role .rule {
    flex: 1; height: 1px; background: var(--cream); position: relative;
  }
  .holder-role .rule::before, .holder-role .rule::after {
    content: ""; position: absolute; top: -2px; width: 5px; height: 5px;
    border-radius: 50%; background: var(--cream);
  }
  .holder-role .rule::before { left: 0; }
  .holder-role .rule::after { right: 0; }

  .contact-list {
    position: absolute; left: 28px; top: 263px; list-style: none;
  }
  .contact-list li {
    display: flex; align-items: center; gap: 14px;
    height: 34px; font-size: 19.5px; color: var(--cream);
  }
  .contact-list svg { width: 20px; height: 20px; fill: var(--tobacco-gold); flex: none; }

  .brand-mark {
    position: absolute; text-align: center;
    font-family: "Roboto", sans-serif; font-weight: 700;
    font-size: 26px; line-height: 1.05; letter-spacing: 1px;
  }
  .card--front .brand-mark { left: 520px; top: 300px; width: 180px; color: var(--cream); }
  .card--back .brand-mark { left: 44px; top: 290px; width: 200px; color: var(--ink); }

  .tagline {
    position: absolute; left: 28px; top: 160px;
    font-family: "Great Vibes", cursive;
    font-size: 60px; color: var(--ink); line-height: 1;
  }
</style>
</head>
<body>
  <section class="card card--front">
    <div class="leaf-art" role="img" aria-label="Faint cigar leaf illustration"></div>
    <h1 class="holder-name">Calvin Rusholm</h1>
    <div class="holder-role"><span class="rule"></span>OWNER<span class="rule"></span></div>
    <ul class="contact-list">
      <li>
        <svg viewBox="0 0 24 24" aria-hidden="true"><path d="M3 8c0-2 4-4 9-4s9 2 9 4v2h-5V8H8v2H3zM6 11h12l3 8H3z"/></svg>
        614-587-3906
      </li>
      <li>
        <svg viewBox="0 0 24 24" aria-hidden="true"><path d="M2 6h20v13H2zM4 8v1l8 5 8-5V8l-8 5z"/></svg>
        crusholm@brevinleafco.com
      </li>
      <li>
        <svg viewBox="0 0 24 24" aria-hidden="true"><path d="M12 2a10 10 0 1 0 0 20 10 10 0 0 0 0-20zm0 2c1 1 2 3 2.3 5H9.7C10 7 11 5 12 4zM4.3 11h3.4a16 16 0 0 0 0 2H4.3a8 8 0 0 1 0-2zm5.4 0h4.6a14 14 0 0 1 0 2H9.7a14 14 0 0 1 0-2zm6.6 0h3.4a8 8 0 0 1 0 2h-3.4a16 16 0 0 0 0-2zM9.7 15h4.6c-.3 2-1.3 4-2.3 5-1-1-2-3-2.3-5z"/></svg>
        brevinkaltwell.com
      </li>
    </ul>
    <div class="brand-mark">BREVIN<br>KALTWELL</div>
  </section>

  <section class="card card--back">
    <div class="leaf-art" role="img" aria-label="Large cigar leaf illustration"></div>
    <p class="tagline">Respect The Smoke</p>
    <div class="brand-mark">BREVIN<br>KALTWELL</div>
  </section>
</body>
</html>
```